Kelvo Marine business card

We sell live saltwater fish and live corals
Kelvo Marine
7 Harlow Ct
Brantley, NJ. 08099
(856) 555-0147
Contact Information for Business Card
Kelvo Marine
7 Harlow Ct
Brantley, NJ. 08099
(856) 555-0147
Colors
Designer to choose colors to be used in the design.

```html
<!DOCTYPE html>
<html lang="en">
<head>
<meta charset="utf-8">
<title>Kelvo Marine – Business Card</title>
<link href="https://fonts.googleapis.com/css2?family=Nunito:wght@600&display=swap" rel="stylesheet">
<style>
  :root {
    --page-bg: #e8e8e8;
    --ocean-deep: #152a6b;
    --ocean-mid: #1a3d9a;
    --ocean-bright: #1f4fb0;
    --coral-glow: #8fb4ee;
    --coral-soft: #5a7fd6;
    --rock-violet: #5b4f9c;
    --text-light: #ffffff;
  }
  html, body {
    margin: 0;
    width: 1200px;
    height: 800px;
    overflow: hidden;
    background: var(--page-bg);
  }
  .business-card {
    position: absolute;
    left: 75px;
    top: 100px;
    width: 1050px;
    height: 600px;
    overflow: hidden;
    background:
      radial-gradient(ellipse 60% 55% at 20% 22%, #1b2c6e 0%, transparent 70%),
      linear-gradient(165deg, var(--ocean-deep) 0%, var(--ocean-mid) 55%, var(--ocean-bright) 100%);
  }
  .coral-photo {
    position: absolute;
    right: 0;
    top: 0;
    width: 560px;
    height: 600px;
    background:
      radial-gradient(ellipse 30% 32% at 40% 36%, var(--coral-glow) 0%, var(--coral-soft) 45%, transparent 78%),
      radial-gradient(ellipse 30% 70% at 100% 60%, var(--rock-violet) 0%, #3b3f8c 50%, transparent 85%),
      radial-gradient(ellipse 25% 20% at 95% 12%, #7a6ab8 0%, transparent 80%);
  }
  .card-details {
    position: absolute;
    left: 76px;
    top: 155px;
    font-family: "Nunito", sans-serif;
    font-weight: 600;
    color: var(--text-light);
    font-size: 46px;
    line-height: 60px;
  }
  .company-name { margin: 0 0 30px; font: inherit; }
  .address { margin: 0 0 12px; }
  .phone { margin: 0; }
</style>
</head>
<body>
  <section class="business-card">
    <div class="coral-photo" role="img" aria-label="Photograph of a glowing blue coral anemone on a violet reef rock underwater"></div>
    <div class="card-details">
      <h1 class="company-name">Kelvo Marine</h1>
      <p class="address">7 Harlow Ct<br>Brantley, NJ. 08099</p>
      <p class="phone">(856) 555-0147</p>
    </div>
  </section>
</body>
</html>
```